Velmoria Blend tea

We are relaunching our new bottle of Guayusa energy tea.
Guayusa is cultivate carefully by The native South American Amazonian farmers, with a diverse mix of food crops, herbs, hardwood trees, fruit trees, spices, medicinal plants and the Guayusa Trees. The farming process that takes place in harmony with the Amazon Rainforest and the diversity of their gardens reflects this attitude toward the natural world.

The company was establish in 2014 and goes by until the pandemic. When all the operations stoped. Now we want to enter again into the USA market with many improvements in the bottle image, we want to use glass bottle so the costumer can look into the color of the tea but with a logo that stand ups, nutritional information and benefits for your health with the Guayusa energy tea
like:
Acecelerate Metabolism
24 Vitamins and Minerals
Burns Calories & Body fat
Provide essential energy

Brewed From Guayusa : used throughout centuries for its healing properties, focused mental clarity, and potent health effects!

Sweetened With Natural Agave :healthy alternative to sugar & artificial sweeteners with a more smooth, flavorful taste than other teas!

Sooth & Stimulating : abundance of caffeine that is slowly released to provide a smooth and pleasant stimulus for waking up in the morning!

Low Glycemic Index :stabilizes blood sugar levels to promote weight loss, boost cardiovascular health & prevent type 2 diabetes!

2 x As Many Antioxidants as Green tea : great for immune system health, eliminating free radicals & fighting/preventing cancer!

Excellent Source of Nutrition — provides an array of 11 polyphenols, 15 amino acids & 24 vitamins and minerals for healthy, balanced diet!

Target Market(s)

eeuu

Industry/Entity Type

beverages industry

Colors
FFC000
F8CF3A
FAE287
FDF2CF
FEFAEE

Requirements
Must have
• Glass bottle designs, full label

```html
<!DOCTYPE html>
<html lang="en">
<head>
<meta charset="utf-8">
<title>Velmoria Blend tea – Amazonian Energy Tea label</title>
<link rel="stylesheet" href="https://fonts.googleapis.com/css2?family=Montserrat:wght@800&family=Mukta:wght@300;400&family=Roboto+Condensed:wght@500&family=Roboto+Slab:wght@800&display=swap">
<style>
  :root {
    --page: #ffffff;
    --band-dark: #2f2117;
    --pattern-light: #f1e8d2;
    --pattern-mid: #dccca8;
    --pattern-warm: #cdb98c;
    --label-cream: #ebe1cc;
    --brown-dark: #2e1f14;
    --brown-mid: #7a5b33;
    --plum: #5c2d3b;
    --rule: #8a6d4a;
    --box: #7b5c34;
    --box-text: #fbf4e4;
    --leaf-green: #7f9a5a;
    --tea-dark: #3d3026;
  }
  * { margin: 0; padding: 0; box-sizing: border-box; }
  html, body { width: 1200px; height: 878px; overflow: hidden; background: var(--page); }
  .canvas { position: relative; width: 1200px; height: 878px; }
  .label {
    position: absolute; left: 369px; top: 0; width: 462px; height: 878px;
    background: var(--label-cream); overflow: hidden;
  }
  .band { position: absolute; left: 0; width: 100%; background: var(--band-dark); }
  .band--top { top: 0; height: 16px; }
  .band--bottom { bottom: 0; height: 12px; }
  .pattern {
    position: absolute; left: 0; top: 16px; width: 100%; height: 411px;
    background: linear-gradient(160deg, var(--pattern-light) 0%, var(--pattern-mid) 45%, var(--pattern-light) 70%, var(--pattern-warm) 100%);
    border-bottom: 3px solid #c9b893;
  }
  .brand {
    position: absolute; left: 0; top: 170px; width: 100%; text-align: center;
    font-family: "Roboto Slab", Georgia, serif; font-weight: 800;
    font-size: 34px; line-height: 1.15; letter-spacing: 2px;
    color: var(--brown-dark); text-transform: uppercase;
  }
  .title {
    position: absolute; left: 0; width: 100%; text-align: center;
    font-family: "Montserrat", Arial, sans-serif; font-weight: 800; font-size: 43px; line-height: 1;
  }
  .title--main { top: 452px; color: var(--brown-dark); }
  .title--sub { top: 499px; color: var(--brown-mid); }
  .rule { position: absolute; left: 75px; width: 312px; height: 1px; background: var(--rule); }
  .rule--upper { top: 555px; }
  .rule--lower { top: 589px; }
  .origin {
    position: absolute; left: 0; top: 559px; width: 100%; text-align: center;
    font-family: "Mukta", Arial, sans-serif; font-weight: 400; font-size: 21px; line-height: 1.2;
    color: var(--plum); letter-spacing: 0.3px;
  }
  .leaf-photo {
    position: absolute; left: 47px; top: 605px; width: 345px; height: 112px;
    background: radial-gradient(ellipse 60% 70% at 60% 65%, var(--tea-dark) 0%, #5a4a3b 55%, rgba(235,225,204,0) 100%),
                radial-gradient(ellipse 30% 40% at 22% 35%, var(--leaf-green) 0%, rgba(235,225,204,0) 100%);
  }
  .benefits {
    position: absolute; left: 29px; top: 753px; width: 406px; height: 66px;
    display: flex; gap: 4px;
  }
  .benefit {
    position: relative; flex: 1; background: var(--box);
    display: flex; align-items: flex-end; justify-content: center; padding-bottom: 8px;
    font-family: "Roboto Condensed", Arial, sans-serif; font-weight: 500;
    font-size: 12.5px; line-height: 1.35; color: var(--box-text); text-align: center;
  }
  .benefit__icon {
    position: absolute; left: 50%; top: -18px; transform: translateX(-50%);
    width: 36px; height: 36px; border-radius: 50%; background: var(--box);
    display: flex; align-items: center; justify-content: center;
  }
  .volume {
    position: absolute; left: 0; top: 828px; width: 100%; text-align: center;
    font-family: "Mukta", Arial, sans-serif; font-weight: 300; font-size: 21px; color: var(--brown-dark);
  }
</style>
</head>
<body>
<div class="canvas">
  <section class="label">
    <div class="band band--top"></div>
    <div class="pattern" role="img" aria-label="Faceted gold and cream triangle pattern"></div>
    <div class="brand">Velmoria<br>Blend tea</div>

    <h1 class="title title--main">AMAZONIAN</h1>
    <h2 class="title title--sub">ENERGY TEA</h2>
    <div class="rule rule--upper"></div>
    <p class="origin">FROM THE GUAYUSA LEAF</p>
    <div class="rule rule--lower"></div>

    <div class="leaf-photo" role="img" aria-label="Photo of a green guayusa leaf beside a pile of dried loose tea"></div>

    <ul class="benefits">
      <li class="benefit">
        <span class="benefit__icon"><svg width="22" height="22" viewBox="0 0 22 22" fill="none" stroke="#fbf4e4" stroke-width="2"><path d="M4 11a7 7 0 0 1 12-5"/><path d="M18 11a7 7 0 0 1-12 5"/><path d="M16 2v4h-4M6 20v-4h4"/></svg></span>
        Acecelerate<br>Metabolism
      </li>
      <li class="benefit">
        <span class="benefit__icon"><svg width="22" height="22" viewBox="0 0 22 22" fill="#fbf4e4"><path d="M8 3c3 4 5 7 5 10a5 5 0 0 1-10 0c0-3 2-6 5-10z"/><circle cx="16" cy="15" r="4.5"/></svg></span>
        24 Vitamins<br>and Minerals
      </li>
      <li class="benefit">
        <span class="benefit__icon"><svg width="22" height="22" viewBox="0 0 22 22" fill="#fbf4e4"><path d="M11 2c1 4 6 6 6 12a6 6 0 0 1-12 0c0-3 2-5 3-7 1 2 2 3 3 3 0-3-1-5 0-8z"/></svg></span>
        Burns Calories<br>&amp; Body fat
      </li>
      <li class="benefit">
        <span class="benefit__icon"><svg width="22" height="22" viewBox="0 0 22 22" fill="#fbf4e4"><path d="M12 2 5 12h5l-1 8 7-10h-5z"/></svg></span>
        Essential<br>Energy
      </li>
    </ul>

    <p class="volume">16fl oz. (473ml)</p>
    <div class="band band--bottom"></div>
  </section>
</div>
</body>
</html>
```